Bright Meadow Dental Lab - Presentation Folder Design

1. We are a dental lab providing a full range of dental products to restore and enhance the natural beauty of the patients’ smiles. We provide fixed restorations (Full-Contour Solid Zirconia, KTR o.lux, Nimbo Core, Full Cast, PFM, Temporary Crowns, Diagnostic Wax-Ups and Study Models), implant restorations (Single and Multi Tooth Restorations, Zirconia Prosthesis, Full Arch Hybrid Prosthesis), and
removable restorations (Dentures and Partials, PliaTek, Sorvent).
2. The target market are dentists, oral surgeons, implant manufacturers, and etc. We are not targeting patients.
3. Design specifics - no specifics, but I have provided our logo for reference if needed

Target Market(s)

Dentists, Oral Surgeons, implant manufacturers

Industry/Entity Type

Dental

Requirements
Must have
• Name - Bright Meadow Dental Lab, address - 4126 Larkspur Ln, Suite 310, Fairbrook, VA 20999, office number - 555-201-0142, fax number - 555-201-0143, email - info@bmdentalstudio.example

```html
<!DOCTYPE html>
<html lang="en">
<head>
<meta charset="utf-8">
<title>Bright Meadow Dental Lab – Presentation Folder</title>
<link rel="stylesheet" href="https://fonts.googleapis.com/css2?family=Montserrat:wght@400;500;600&display=swap">
<style>
  :root {
    --stage: #b3b3b5;
    --navy: #2d2f8e;
    --navy-deep: #25277a;
    --sky: #86c6e4;
    --teal: #2b8296;
    --white: #ffffff;
    --paper: #f6f6f8;
    --faint: #dcdcec;
    --photo-a: #e9dcd3;
    --photo-b: #c79aa8;
  }
  * { box-sizing: border-box; margin: 0; padding: 0; }
  html, body { width: 842px; height: 1200px; overflow: hidden; }
  body {
    background: var(--stage);
    font-family: "Montserrat", Arial, sans-serif;
    position: relative;
  }
  .spread { position: absolute; left: 51px; width: 740px; height: 500px; display: flex; }
  .spread--outside { top: 50px; }
  .spread--inside { top: 640px; }
  .panel { position: relative; width: 370px; height: 500px; overflow: hidden; }
  .panel svg.shapes { position: absolute; inset: 0; }

  .brand-name {
    font-weight: 600; letter-spacing: 0.5px; line-height: 1.15; text-transform: uppercase;
  }
  .web {
    position: absolute; left: 0; right: 0; bottom: 26px;
    font-size: 12px; letter-spacing: 1px; color: var(--white); text-align: center;
  }

  /* back cover */
  .back-cover { background: var(--navy); color: var(--white); text-align: center; }
  .back-cover .smile-photo {
    position: absolute; left: 128px; top: 70px; width: 114px; height: 114px;
    border-radius: 50%; border: 5px solid var(--teal);
    background: radial-gradient(circle at 50% 55%, var(--paper) 0 18%, var(--photo-b) 40%, var(--photo-a) 100%);
  }
  .back-cover .brand-name { position: absolute; top: 215px; left: 0; right: 0; font-size: 24px; color: var(--white); }
  .back-cover .contact {
    position: absolute; top: 318px; left: 0; right: 0;
    font-size: 12px; line-height: 1.55; font-weight: 400;
  }
  .contact b { font-weight: 600; }

  /* front cover */
  .front-cover { background: var(--photo-a); }
  .front-cover .cover-photo {
    position: absolute; inset: 0;
    background: linear-gradient(160deg, #eef1f0 0%, var(--photo-a) 45%, var(--photo-b) 100%);
  }
  .front-cover .brand-name {
    position: absolute; top: 28px; left: 150px; right: 24px;
    font-size: 22px; color: var(--navy); text-align: center;
  }

  /* inside */
  .inside-panel { background: var(--paper); border-left: 1px solid #e3e3ea; }
  .inside-panel .brand-name {
    position: absolute; top: 70px; left: 30px; right: 30px;
    font-size: 30px; color: var(--faint); text-align: center;
  }
  .pocket {
    position: absolute; left: 0; right: 0; bottom: 0; height: 170px;
    background: linear-gradient(180deg, var(--navy-deep), var(--navy));
    box-shadow: 0 -3px 6px rgba(0,0,0,0.15);
  }
</style>
</head>
<body>

<section class="spread spread--outside">
  <article class="panel back-cover">
    <svg class="shapes" width="370" height="500" viewBox="0 0 370 500" aria-hidden="true">
      <path d="M0 440 Q230 460 370 360" fill="none" stroke="var(--teal)" stroke-width="4"/>
    </svg>
    <div class="smile-photo" role="img" aria-label="Close-up photo of a smile with a clear aligner"></div>
    <h2 class="brand-name">Bright Meadow<br>Dental Lab</h2>
    <p class="contact">
      4126 Larkspur Ln, Suite 310,<br>
      Fairbrook, VA 20999<br>
      <b>(P)</b> 555-201-0142 <b>(F)</b> 555-201-0143<br>
      info@bmdentalstudio.example
    </p>
    <p class="web">WWW.BMDENTALSTUDIO.EXAMPLE</p>
  </article>

  <article class="panel front-cover">
    <div class="cover-photo" role="img" aria-label="Photo of a smiling young woman pointing at her teeth"></div>
    <svg class="shapes" width="370" height="500" viewBox="0 0 370 500" aria-hidden="true">
      <path d="M0 0 C110 140 250 150 370 130 V142 C250 164 100 156 0 14 Z" fill="var(--teal)"/>
      <path d="M0 0 H370 V130 C250 150 110 140 0 0 Z" fill="var(--sky)"/>
      <path d="M0 430 Q180 380 370 410 V500 H0 Z" fill="var(--navy)"/>
    </svg>
    <h1 class="brand-name">Bright Meadow<br>Dental Lab</h1>
    <p class="web">WWW.BMDENTALSTUDIO.EXAMPLE</p>
  </article>
</section>

<section class="spread spread--inside">
  <article class="panel inside-panel">
    <p class="brand-name">Bright Meadow<br>Dental Lab</p>
    <div class="pocket"></div>
  </article>
  <article class="panel inside-panel">
    <p class="brand-name">Bright Meadow<br>Dental Lab</p>
    <div class="pocket"></div>
  </article>
</section>

</body>
</html>
```